Coralbay Realty Letterhead

Coralbay Realty Guan
418 Maru Tasi Loop, Ste B207
Tumon, GU. 96928

Industry/Entity Type

Real Estate

Font styles to use
Serif

Colors

Designer to choose colors to be used in the design.

```html
<!DOCTYPE html>
<html lang="en">
<head>
<meta charset="utf-8">
<title>Coralbay Realty Letterhead</title>
<link href="https://fonts.googleapis.com/css2?family=Cormorant+Garamond:wght@500&family=Montserrat:wght@400;600&family=Open+Sans:wght@500&display=swap" rel="stylesheet">
<style>
  :root {
    --backdrop: #e8e9eb;
    --paper: #ffffff;
    --ink: #1f1f24;
    --ocean-deep: #1995d4;
    --ocean-light: #6ecbeb;
    --sky: #3fb4e4;
  }
  * { margin: 0; padding: 0; box-sizing: border-box; }
  html, body {
    width: 1200px; height: 900px; overflow: hidden;
    background: var(--backdrop);
  }
  .letterhead {
    position: absolute; left: 270px; top: 22px;
    width: 660px; height: 855px;
    background: var(--paper);
    overflow: hidden;
    font-family: "Montserrat", sans-serif;
    color: var(--ink);
  }
  .brand {
    position: absolute; top: 88px; left: 0; width: 100%;
    display: flex; justify-content: center; align-items: center; gap: 14px;
  }
  .brand-dot {
    width: 16px; height: 16px; border-radius: 50%;
    background: var(--sky);
  }
  .brand-name {
    font-family: "Cormorant Garamond", serif;
    font-weight: 500; font-size: 42px; letter-spacing: 2px;
    color: var(--sky); line-height: 1;
  }
  .letter-body {
    position: absolute; left: 38px; top: 206px; width: 586px;
  }
  .date, .salutation, .closing, .signatory {
    font-weight: 600; font-size: 10.5px; letter-spacing: 0.5px;
  }
  .salutation { margin-top: 17px; }
  .paragraph {
    font-size: 10.4px; line-height: 16.3px; letter-spacing: 0.62px;
    text-align: justify; margin-top: 16px;
  }
  .salutation + .paragraph { margin-top: 32px; }
  .closing { margin-top: 18px; }
  .signature {
    margin-top: 14px; width: 196px; height: 40px;
    background: linear-gradient(90deg, rgba(63,180,228,0.18), rgba(63,180,228,0.06));
    border-radius: 4px;
  }
  .signatory { margin-top: 22px; }
  .footer-band {
    position: absolute; left: 0; bottom: 0; width: 660px; height: 205px;
    background: linear-gradient(180deg, rgba(110,203,235,0) 0%, var(--ocean-light) 32%, var(--ocean-deep) 62%);
  }
  .address {
    position: absolute; left: 38px; top: 796px;
    font-family: "Open Sans", sans-serif; font-weight: 500; font-style: normal;
    font-size: 10.5px; line-height: 17px; color: var(--paper);
  }
</style>
</head>
<body>
  <main class="letterhead">
    <header class="brand">
      <span class="brand-dot"></span>
      <span class="brand-name">Coralbay Realty</span>
    </header>

    <section class="letter-body">
      <p class="date">Monday, January 05, 2023</p>
      <p class="salutation">Dear Madam/Sir</p>
      <p class="paragraph">Lorem ipsum dolor sit amet, consectetur adipiscing elit, sed do eiusmod tempor incididunt ut labore et dolore magna aliqua. Ut enim ad minim veniam, quis nostrud exercitation ullamco laboris nisi ut aliquip ex ea commodo consequat. Duis aute irure dolor in reprehenderit in voluptate velit esse cillum dolore eu fugiat nulla pariatur. Excepteur sint occaecat cupidatat non proident, sunt in culpa qui officia deserunt mollit anim id est laborum.</p>
      <p class="paragraph">Curabitur pretium tincidunt lacus. Nulla gravida orci a odio. Nullam varius, turpis et commodo pharetra, est eros bibendum elit, nec luctus magna felis sollicitudin mauris. Integer in mauris eu nibh euismod gravida. Duis ac tellus et risus vulputate vehicula. Donec lobortis risus a elit. Etiam tempor. Ut ullamcorper, ligula eu tempor congue, eros est euismod turpis, id tincidunt sapien risus a quam.</p>
      <p class="paragraph">Maecenas fermentum consequat mi. Donec fermentum. Pellentesque malesuada nulla a mi. Duis sapien sem, aliquet nec, commodo eget, consequat quis, neque. Aliquam faucibus, elit ut dictum aliquet, felis nisl adipiscing sapien, sed malesuada diam lacus eget erat. Cras mollis scelerisque nunc. Nullam arcu. Aliquam consequat. Curabitur augue lorem, dapibus quis, laoreet et, pretium ac, nisi. Aenean magna nisl, mollis quis, molestie eu, feugiat in, orci. In hac habitasse platea dictumst.</p>
      <p class="closing">Sincerely,</p>
      <div class="signature" role="img" aria-label="Handwritten signature of Lior Vantessa"></div>
      <p class="signatory">Mr. Lior Vantessa</p>
    </section>

    <div class="footer-band" role="img" aria-label="Decorative ocean wave and water splash illustration in light and deep blue"></div>

    <address class="address">418 Maru Tasi Loop, Ste B207<br>Tumon, GU. 96928</address>
  </main>
</body>
</html>
```